Bluestone Advisory & Mgmt - Professional Business Cards

Hi!

I am a Real Estate Developer and Construction Consultant.

I have a lot of inspiration from previous designs and would be open to using the attached Designs as a starting point. I would like to see these styles incorporated into your designs.

I really need professional business card to go with it that includes my important info.

Look forward to seeing your designs!.

Target Market(s)

My Target market are building owners, lawyers, consultants.

Industry/Entity Type

Real Estate Development

Contact Information for Business Card

My Name: Dorian Pelkey
My Title: Principle
Company Name: Bluestone Advisory & Mgmt, LLC
Address: 348 Westbrook Lane, 9th FL Harlow Point, ZZ 00000
Mobile: 555.806.3971
Website: bam-hvx.example

Font styles to use
Serif
Sans Serif

Colors

Designer to choose colors to be used in the design.

Requirements
Must have
• Must incorporate the logo attached or have new that looks similar.
• Must use professional font that will be seen and judged by wealthy land owners and developers.
• Must incorporate some of the color green.
Should not have
• Photo's or pictures of people or buildings of any kind.

```html
<!DOCTYPE html>
<html lang="en">
<head>
<meta charset="utf-8">
<title>Bluestone Advisory &amp; Mgmt – Business Cards</title>
<link rel="stylesheet" href="https://fonts.googleapis.com/css2?family=Raleway:wght@400;700&family=Roboto:wght@400&display=swap">
<style>
  :root {
    --canvas: #e4e4e4;
    --green: #43b06f;
    --green-soft: #4fb879;
    --paper: #f1f1f1;
    --ink: #3e3e3e;
    --white: #ffffff;
  }
  * { margin: 0; padding: 0; box-sizing: border-box; }
  html, body { width: 1200px; height: 884px; overflow: hidden; }
  body {
    background: var(--canvas);
    position: relative;
    font-family: "Roboto", sans-serif;
  }
  .card {
    position: absolute;
    left: 250px;
    width: 700px;
    height: 391px;
    overflow: hidden;
  }
  .card--front { top: 34px; background: var(--green); }
  .card--back { top: 459px; background: var(--paper); }

  /* front */
  .map-area {
    position: absolute;
    left: 6px; top: 44px;
    width: 676px; height: 330px;
    border-radius: 40px;
    background: radial-gradient(ellipse at 40% 50%, var(--green-soft) 0%, var(--green) 70%);
  }
  .front-name {
    position: absolute;
    left: 200px; top: 212px;
    font-family: "Raleway", sans-serif;
    font-weight: 400;
    color: var(--white);
    line-height: 1.05;
  }
  .front-name__main { display: block; font-size: 58px; }
  .front-name__sub { display: block; font-size: 27px; margin-top: 6px; }

  /* back */
  .accent-bar {
    position: absolute;
    left: 0; top: 53px;
    width: 18px; height: 37px;
    background: var(--green);
  }
  .person { position: absolute; left: 52px; top: 51px; }
  .person__name {
    font-family: "Raleway", sans-serif;
    font-weight: 700;
    font-size: 22px;
    color: var(--green);
    text-transform: uppercase;
    letter-spacing: 0.2px;
    line-height: 1.1;
  }
  .person__title { font-size: 20px; color: var(--ink); line-height: 1.3; }

  .contacts { position: absolute; left: 52px; top: 119px; list-style: none; }
  .contacts li {
    display: flex; align-items: center; gap: 6px;
    font-size: 19px; color: var(--ink);
    height: 26.5px; letter-spacing: 0.4px;
  }
  .contacts svg { width: 19px; height: 19px; flex: none; }
  .contacts .hl { color: var(--green); }

  .address {
    position: absolute; left: 52px; top: 289px;
    font-size: 19px; color: var(--ink);
    line-height: 1.3; font-style: normal; letter-spacing: 0.4px;
  }

  .brand {
    position: absolute; left: 462px; top: 290px;
    font-family: "Raleway", sans-serif;
    font-weight: 400;
    color: var(--green);
    line-height: 1.05;
  }
  .brand__main { display: block; font-size: 38px; }
  .brand__sub { display: block; font-size: 17px; margin-top: 2px; }
</style>
</head>
<body>
  <section class="card card--front" aria-label="Card front">
    <div class="map-area" role="img" aria-label="Faint dotted world map pattern in light green"></div>
    <div class="front-name">
      <span class="front-name__main">Bluestone</span>
      <span class="front-name__sub">Advisory &amp; Mgmt</span>
    </div>
  </section>

  <section class="card card--back" aria-label="Card back">
    <div class="accent-bar"></div>
    <div class="person">
      <p class="person__name">Dorian Pelkey</p>
      <p class="person__title">Principle</p>
    </div>
    <ul class="contacts">
      <li>
        <svg viewBox="0 0 24 24" aria-hidden="true"><path fill="var(--green)" d="M6.6 10.8a15.1 15.1 0 0 0 6.6 6.6l2.2-2.2c.3-.3.7-.4 1-.2 1.1.4 2.3.6 3.6.6.6 0 1 .4 1 1V20c0 .6-.4 1-1 1A17 17 0 0 1 3 4c0-.6.4-1 1-1h3.5c.6 0 1 .4 1 1 0 1.3.2 2.5.6 3.6.1.3 0 .7-.2 1z"/></svg>
        555.806.3971
      </li>
      <li>
        <svg viewBox="0 0 24 24" aria-hidden="true"><rect x="2" y="5" width="20" height="14" fill="var(--green)"/><path d="M2 5l10 8 10-8M2 19l7-7M22 19l-7-7" stroke="var(--paper)" stroke-width="1.5" fill="none"/></svg>
        info@bam-hvx.example
      </li>
      <li>
        <svg viewBox="0 0 24 24" aria-hidden="true"><circle cx="12" cy="12" r="10" fill="var(--green)"/><path d="M2 12h20M12 2c3 3 3 17 0 20M12 2c-3 3-3 17 0 20" stroke="var(--paper)" stroke-width="1.3" fill="none"/></svg>
        <span>www.<span class="hl">bam-hvx</span>.example</span>
      </li>
    </ul>
    <address class="address">
      348 Westbrook Lane,<br>
      9th FL Harlow Point, ZZ 00000
    </address>
    <div class="brand">
      <span class="brand__main">Bluestone</span>
      <span class="brand__sub">Advisory &amp; Mgmt</span>
    </div>
  </section>
</body>
</html>
```